Quillo Business Card Design

Looking for elegant and super stylish business cards. Enclosed is the card design we are using now. We need something more contemporary.

Target Market(s)

We are a catering company focusing on weddings and corporate events.

Industry/Entity Type

Caterer

Contact Information for Business Card

Please use similar font to our current cards

Colors
0592cd

Requirements
Must have
• Color and be very unique. Also, please use logo (with or without the castle.)

```html
<!DOCTYPE html>
<html lang="en">
<head>
<meta charset="utf-8">
<title>Quillo Business Card</title>
<link href="https://fonts.googleapis.com/css2?family=Roboto:wght@300;400;500&display=swap" rel="stylesheet">
<style>
  :root {
    --backdrop: #8a8a8a;
    --accent: #0592cd;
    --paper: #e9e7e3;
    --paper-ink: #5b5b5b;
    --paper-ink-strong: #4a4a4a;
    --slate-top: #3a3a3a;
    --slate-bottom: #1c1c1c;
    --slate-ink: #d6d6d6;
    --slate-ink-soft: #a9a9a9;
  }
  html, body {
    margin: 0;
    padding: 0;
    width: 1200px;
    height: 900px;
    overflow: hidden;
    background: var(--backdrop);
  }
  .stage {
    width: 1200px;
    height: 900px;
    display: flex;
    align-items: center;
    justify-content: center;
    gap: 90px;
  }
  .card {
    width: 340px;
    height: 595px;
    border-radius: 26px;
    box-sizing: border-box;
    box-shadow: 0 18px 40px rgba(0,0,0,0.35);
    display: flex;
    flex-direction: column;
    align-items: center;
    text-align: center;
    font-family: "Roboto", sans-serif;
  }

  /* Contact side */
  .card--contact {
    background: var(--paper);
    color: var(--paper-ink);
    padding-top: 52px;
  }
  .holder-name {
    font-size: 19px;
    font-weight: 500;
    letter-spacing: 0.5px;
    color: var(--accent);
    margin: 0;
  }
  .holder-title {
    font-size: 14px;
    font-weight: 400;
    margin: 6px 0 0;
  }
  .brand-word {
    font-weight: 400;
    font-size: 40px;
    color: var(--paper-ink-strong);
    margin: 48px 0 0;
    letter-spacing: 1px;
  }
  .address {
    font-size: 15px;
    line-height: 1.35;
    margin: 62px 0 0;
  }
  .contact-list {
    list-style: none;
    padding: 0;
    margin: 26px 0 0;
    display: flex;
    flex-direction: column;
    align-items: center;
    gap: 8px;
  }
  .contact-list li {
    display: flex;
    flex-direction: column;
    align-items: center;
    gap: 6px;
    font-size: 15px;
  }
  .contact-icon {
    width: 20px;
    height: 20px;
  }
  .card-tick {
    width: 14px;
    height: 2px;
    background: var(--accent);
    margin-top: 14px;
  }

  /* Brand side */
  .card--brand {
    background: linear-gradient(160deg, var(--slate-top), var(--slate-bottom));
    color: var(--slate-ink);
    padding-top: 62px;
  }
  .brand-mark {
    width: 78px;
    height: 78px;
    border: 2px solid var(--accent);
    box-sizing: border-box;
  }
  .brand-title {
    font-weight: 400;
    font-size: 38px;
    margin: 26px 0 0;
    letter-spacing: 1px;
    color: #ececec;
  }
  .brand-tagline {
    font-weight: 300;
    font-size: 13px;
    letter-spacing: 6px;
    line-height: 1.5;
    margin: 8px 0 0;
    color: var(--accent);
  }
  .service-list {
    list-style: none;
    padding: 0;
    margin: 30px 0 0;
    font-weight: 300;
    font-size: 15px;
    line-height: 2.05;
    color: var(--slate-ink);
  }
  .partner-badge {
    background: var(--slate-ink-soft);
    opacity: 0.85;
  }
  .partner-badge--wide {
    width: 110px;
    height: 34px;
    border-radius: 4px;
    margin-top: 30px;
  }
  .partner-badge--round {
    width: 46px;
    height: 46px;
    border-radius: 50%;
    margin-top: 22px;
  }
</style>
</head>
<body>
<main class="stage">
  <section class="card card--contact">
    <h1 class="holder-name">MAREK OLSTEN</h1>
    <p class="holder-title">Chief Executive Officer</p>
    <p class="brand-word">Quillo</p>
    <p class="address">4410 Harlow Street<br>Bayview, California 90210</p>
    <ul class="contact-list">
      <li>
        <svg class="contact-icon" viewBox="0 0 20 20" aria-hidden="true"><circle cx="10" cy="10" r="9" fill="none" stroke="#0592cd" stroke-width="1.3"/><path d="M7 5.5c-.8.5-1 1.6-.5 2.8.9 2 2.3 3.5 4.3 4.3 1.2.5 2.2.3 2.8-.5l-1.6-1.4-1 .7c-1-.5-1.8-1.3-2.3-2.3l.7-1z" fill="#0592cd"/></svg>
        <span>555 310 4482 ext. 214</span>
      </li>
      <li>
        <svg class="contact-icon" viewBox="0 0 20 20" aria-hidden="true"><circle cx="10" cy="10" r="9" fill="none" stroke="#0592cd" stroke-width="1.3"/><rect x="6" y="6" width="8" height="3" fill="#0592cd"/><rect x="5" y="9" width="10" height="4" rx="1" fill="#0592cd"/><rect x="7" y="12" width="6" height="2.5" fill="#0592cd"/></svg>
        <span>555 718 2093</span>
      </li>
      <li>
        <svg class="contact-icon" viewBox="0 0 20 20" aria-hidden="true"><circle cx="10" cy="10" r="9" fill="none" stroke="#0592cd" stroke-width="1.3"/><rect x="5.5" y="7" width="9" height="6.5" fill="#0592cd"/><path d="M5.5 7l4.5 3.5L14.5 7" fill="none" stroke="#e9e7e3" stroke-width="0.9"/></svg>
        <span>m@quillocatering.com</span>
      </li>
      <li>
        <svg class="contact-icon" viewBox="0 0 20 20" aria-hidden="true"><circle cx="10" cy="10" r="9" fill="none" stroke="#0592cd" stroke-width="1.3"/><circle cx="10" cy="10" r="4.5" fill="none" stroke="#0592cd" stroke-width="1.2"/><path d="M5.5 10h9M10 5.5c-1.8 2.5-1.8 6.5 0 9M10 5.5c1.8 2.5 1.8 6.5 0 9" fill="none" stroke="#0592cd" stroke-width="0.9"/></svg>
        <span>www.quillocatering.com</span>
      </li>
    </ul>
    <div class="card-tick"></div>
  </section>

  <section class="card card--brand">
    <div class="brand-mark" role="img" aria-label="Brand mark placeholder"></div>
    <h2 class="brand-title">The Quillo</h2>
    <p class="brand-tagline">CATERING &amp;<br>EVENT DESIGN</p>
    <ul class="service-list">
      <li>Catering | Event Design</li>
      <li>All-inclusive Packages</li>
      <li>Private Event Venue Management</li>
    </ul>
    <div class="partner-badge partner-badge--wide" role="img" aria-label="Partner venue badge"></div>
    <div class="partner-badge partner-badge--round" role="img" aria-label="Partner club badge"></div>
  </section>
</main>
</body>
</html>
```